Business card for Luxury Portable Restroom Trailer company

We are a Luxury Portable Restroom Trailer Company Called PELIKAR HIRES. Based in Orange County California. We provide portable restroom trailers for events, such as, Weddings, Concerts, Charity events, Sporting events, Tournaments, Corporate events, ect. We rent and Sell the Luxury restrooms. Our colors are white, grey, and Orange. As you will see in the logo we uploaded.
There are 2 people in the company so the names and titles will change for the 3 people but card will remain the same. Here is the information for each Person: Dennis Moyle CFO 555 018-3647
next Person: Wesley Tanford VP 555 018-3647
Next Person: Miles Tanford CEO 555 018-3647
Information to include on the card: Luxury Restroom Trailers Rental and Sales. Weddings, Concerts, Charity, Sporting and Corp. Events.

```html
<!DOCTYPE html>
<html lang="en">
<head>
<meta charset="utf-8">
<title>Pelikar Hires — Business Card</title>
<link rel="stylesheet" href="https://fonts.googleapis.com/css2?family=Montserrat:wght@400;500;700;800&display=swap">
<style>
  :root {
    --orange: #f26d26;
    --grey: #58595b;
    --white: #ffffff;
    --ink: #1f1f1f;
    --backdrop: #eceeee;
  }
  * { margin: 0; padding: 0; box-sizing: border-box; }
  html, body { width: 1179px; height: 1200px; overflow: hidden; }
  body {
    background: var(--backdrop);
    font-family: "Montserrat", Arial, sans-serif;
    position: relative;
  }
  .card {
    position: absolute;
    left: 221px;
    width: 738px;
    height: 423px;
    background: var(--white);
    overflow: hidden;
  }
  .card--front { top: 161px; }
  .card--back { top: 618px; }

  /* Front */
  .front-band {
    position: absolute; left: 0; top: 0;
    width: 506px; height: 100%;
    background: var(--orange);
  }
  .front-wordmark {
    position: absolute; left: 36px; top: 46px;
    color: var(--white);
    font-weight: 800;
    font-size: 31px;
    letter-spacing: 1px;
    line-height: 1;
  }
  .person { position: absolute; left: 36px; color: var(--white); }
  .person__name {
    font-weight: 700; font-size: 22px; line-height: 1; letter-spacing: 0.3px;
    text-transform: uppercase;
  }
  .person__title {
    font-weight: 400; font-size: 18px; line-height: 1; margin-top: 9px;
  }
  .person__phone {
    display: flex; align-items: center; gap: 8px;
    font-weight: 500; font-size: 18px; line-height: 1; margin-top: 10px;
  }
  .person__phone svg { width: 18px; height: 14px; fill: var(--white); }
  .person--1 { top: 130px; }
  .person--2 { top: 218px; }
  .person--3 { top: 310px; }

  .front-emblem {
    position: absolute;
    left: 370px; top: 53px;
    width: 328px; height: 328px;
  }

  /* Back */
  .back-wordmark {
    position: absolute; left: 0; right: 0; top: 146px;
    text-align: center;
    color: var(--grey);
    font-weight: 800;
    font-size: 62px;
    letter-spacing: 2px;
    line-height: 1;
  }
  .services {
    position: absolute; left: 0; right: 0; top: 321px;
    text-align: center;
    color: var(--ink);
    font-size: 18.5px; font-weight: 500; line-height: 27px;
  }
  .services__item { white-space: nowrap; margin: 0 6px; }
  .services__item::before {
    content: ""; display: inline-block;
    width: 11px; height: 11px; border-radius: 50%;
    background: var(--orange);
    margin-right: 9px; vertical-align: 1px;
  }
</style>
</head>
<body>
  <section class="card card--front" aria-label="Card front">
    <div class="front-band"></div>
    <div class="front-wordmark">PELIKAR HIRES</div>

    <div class="person person--1">
      <div class="person__name">Dennis Moyle</div>
      <div class="person__title">CFO</div>
      <div class="person__phone"><svg viewBox="0 0 18 14" aria-hidden="true"><path d="M1 4c0-2 3-3 8-3s8 1 8 3v1h-4V3.5H5V5H1z M4 6h10l2 7H2z"/></svg>555 018-3647</div>
    </div>
    <div class="person person--2">
      <div class="person__name">Wesley Tanford</div>
      <div class="person__title">VP</div>
      <div class="person__phone"><svg viewBox="0 0 18 14" aria-hidden="true"><path d="M1 4c0-2 3-3 8-3s8 1 8 3v1h-4V3.5H5V5H1z M4 6h10l2 7H2z"/></svg>555 018-3647</div>
    </div>
    <div class="person person--3">
      <div class="person__name">Miles Tanford</div>
      <div class="person__title">CEO</div>
      <div class="person__phone"><svg viewBox="0 0 18 14" aria-hidden="true"><path d="M1 4c0-2 3-3 8-3s8 1 8 3v1h-4V3.5H5V5H1z M4 6h10l2 7H2z"/></svg>555 018-3647</div>
    </div>

    <svg class="front-emblem" viewBox="0 0 328 328" role="img" aria-label="Company emblem area">
      <circle cx="164" cy="164" r="164" fill="var(--white)"/>
      <circle cx="164" cy="164" r="144" fill="none" stroke="var(--orange)" stroke-width="15"/>
    </svg>
  </section>

  <section class="card card--back" aria-label="Card back">
    <div class="back-wordmark">PELIKAR HIRES</div>
    <div class="services">
      <div><span class="services__item">Luxury Restroom Trailers Rental and Sales</span></div>
      <div>
        <span class="services__item">Weddings</span>
        <span class="services__item">Concerts</span>
        <span class="services__item">Charity</span>
        <span class="services__item">Sporting and Corp</span>
        <span class="services__item">Events</span>
      </div>
    </div>
  </section>
</body>
</html>
```